Business Card for Marco Thieblin Analytics and Marco Thieblin Photography

I want a double sided business card: on one side it should be about "Marco Thieblin Photography" and on the other side about "Marco Thieblin Analytics". You find the logos for these two projects in the attachments. The design of the business card should blend well with the colours and fonts used in the logos and should be quite simple, yet look professional and modern.

In addition to my name, there should be content for a telephone number, e-mail address and website. There should be little icons (for telephone, email and web) before these fields. I do not want a postal mail address field.
Lastly you should indicate that people can contact me in the following languages: Lëtzebuergesch, Deutsch, Français, English, Castellano, Ido
This should be very unobtrusive: either in a small muted font or with little icons (preferably without using flags as flags represent nations, not languages - one possibility would be by using the 2 letter ISO codes).

The design should be delivered in Adobe Illustrator format or something similar that I can edit easily, as it's possible that I will change my e-mail address and domain soon.

I hope this was detailed enough but still leaves you some freedom for designing something nice.

Thank you!
Marco

Industry/Entity Type

Business

Contact Information for Business Card

e-mail address: mtb_@orvenmail.example
website: www.marcothieblin.example (for Marco Thieblin Photography)
website: kelvodata.example/mtb (for Marco Thieblin Analytics - this address is likely to change)
phone: +352 691 987 654 (not my real number - I prefer not to publish it on the web)

Requirements
Nice to have
• A speech bubble followed by the 2-letter language codes (lb, de, fr, en, es, io) or even speech bubble icons for every language would be nice and eliminates the need to put text like 'you can contact me in the following languages'.

```html
<!DOCTYPE html>
<html lang="en">
<head>
<meta charset="utf-8">
<title>Marco Thieblin – Business Card</title>
<link rel="stylesheet" href="https://fonts.googleapis.com/css2?family=PT+Serif:wght@400;700&display=swap">
<style>
  :root {
    --backdrop: #1f1f1f;
    --card-dark: #050505;
    --card-light: #faf8f4;
    --orange: #f0862a;
    --green: #1e9e4a;
    --ink: #2b2b2b;
    --muted: #444444;
    --rule: #3a3a3a;
  }
  * { box-sizing: border-box; margin: 0; padding: 0; }
  html, body {
    width: 1200px; height: 1000px; overflow: hidden;
    background: var(--backdrop);
    font-family: "PT Serif", Georgia, serif;
  }
  .stage {
    position: relative; width: 1200px; height: 1000px;
  }
  .card {
    position: absolute; top: 345px;
    width: 540px; height: 310px;
    box-shadow: 0 6px 18px rgba(0,0,0,.45);
  }
  /* Photography side */
  .card--photography {
    left: 45px; background: var(--card-dark);
    display: flex; align-items: center; justify-content: center; gap: 14px;
  }
  .brand-dot {
    width: 26px; height: 26px; border-radius: 50%;
    background: var(--orange);
  }
  .brand-name--photography {
    color: var(--orange); font-size: 28px; font-weight: 400;
  }
  /* Analytics side */
  .card--analytics {
    left: 615px; background: var(--card-light);
  }
  .brand-name--analytics {
    position: absolute; left: 38px; top: 98px;
    color: var(--orange); font-size: 21px; font-weight: 400;
    display: flex; align-items: center; gap: 10px;
  }
  .brand-square {
    width: 16px; height: 16px; background: var(--orange);
  }
  .contact {
    position: absolute; left: 318px; top: 112px;
  }
  .contact__name {
    color: var(--green); font-size: 22px; font-weight: 700;
    margin-bottom: 8px;
  }
  .contact__list { list-style: none; }
  .contact__item {
    display: flex; align-items: center; gap: 8px;
    color: var(--ink); font-size: 14px; font-weight: 700;
    line-height: 20px;
  }
  .contact__icon { width: 12px; height: 12px; flex: none; }
  .divider {
    position: absolute; left: 36px; right: 36px; top: 222px;
    border-top: 1.5px solid var(--rule);
  }
  .languages {
    position: absolute; left: 36px; right: 36px; top: 236px;
    text-align: center; color: var(--muted); font-size: 11.5px;
  }
</style>
</head>
<body>
<main class="stage">
  <section class="card card--photography" aria-label="Photography side">
    <span class="brand-dot"></span>
    <span class="brand-name--photography">Marco Thieblin Photography</span>
  </section>

  <section class="card card--analytics" aria-label="Analytics side">
    <div class="brand-name--analytics">
      <span class="brand-square"></span>
      <span>Marco Thieblin Analytics</span>
    </div>

    <div class="contact">
      <p class="contact__name">Marco Thieblin</p>
      <ul class="contact__list">
        <li class="contact__item">
          <svg class="contact__icon" viewBox="0 0 12 12" aria-hidden="true"><path d="M3 1 L5 3.5 L4 5 Q5.5 7.5 7 8 L8.5 7 L11 9 L9.5 11 Q4 10.5 1 3 Z" fill="var(--orange)"/></svg>
          <span>1 (555) 014-2290</span>
        </li>
        <li class="contact__item">
          <svg class="contact__icon" viewBox="0 0 12 12" aria-hidden="true"><rect x="0.5" y="2" width="11" height="8" fill="var(--orange)"/><path d="M0.5 2 L6 6.5 L11.5 2" fill="none" stroke="var(--card-light)" stroke-width="1"/></svg>
          <span>mtb_@orvenmail.example</span>
        </li>
        <li class="contact__item">
          <svg class="contact__icon" viewBox="0 0 12 12" aria-hidden="true"><circle cx="6" cy="6" r="5.3" fill="none" stroke="var(--orange)" stroke-width="1.3"/><ellipse cx="6" cy="6" rx="2.2" ry="5.3" fill="none" stroke="var(--orange)" stroke-width="1"/><line x1="0.7" y1="6" x2="11.3" y2="6" stroke="var(--orange)" stroke-width="1"/></svg>
          <span>www.marcothieblin.example</span>
        </li>
      </ul>
    </div>

    <div class="divider"></div>
    <p class="languages">Lëtzebuergesch, Deutsch, Français, English, Castellano, Ido</p>
  </section>
</main>
</body>
</html>
```